Ridgeline Journeys business card

please see website
www.ridgelinejourneys.comau

info needed on card
Kieran Folsby
Ph
email
Adventure Riding GPS trails

please use my logo and colours off my site

Industry/Entity Type

Business

Contact Information for Business Card

Kieran Folsby
kieran@ridgelinejourneys.com

```html
<!DOCTYPE html>
<html lang="en">
<head>
<meta charset="utf-8">
<title>Ridgeline Journeys – Business Card</title>
<link href="https://fonts.googleapis.com/css2?family=Open+Sans:wght@400;600;700&display=swap" rel="stylesheet">
<style>
  :root {
    --backdrop: #d9d9d7;
    --card-top: #1c1c1c;
    --card-bottom: #0c0c0c;
    --accent: #f7c600;
    --text-light: #f2f2f2;
    --rule-dark: #2c2c2c;
    --card-shadow: rgba(0, 0, 0, 0.25);
  }
  * { box-sizing: border-box; margin: 0; padding: 0; }
  html, body {
    width: 1200px;
    height: 900px;
    overflow: hidden;
    background: var(--backdrop);
    font-family: "Open Sans", Arial, sans-serif;
  }
  .canvas {
    position: relative;
    width: 1200px;
    height: 900px;
  }
  .card {
    position: absolute;
    left: 250px;
    width: 700px;
    height: 400px;
    background: radial-gradient(ellipse at 55% 35%, var(--card-top), var(--card-bottom) 80%);
    box-shadow: 0 6px 18px var(--card-shadow);
    overflow: hidden;
  }
  .card--back { top: 40px; }
  .card--front { top: 465px; }

  /* Back card */
  .back-mark {
    position: absolute;
    left: 0; right: 0;
    top: 120px;
    display: flex;
    justify-content: center;
    align-items: center;
    gap: 16px;
  }
  .mark-dot {
    width: 34px;
    height: 34px;
    border-radius: 50%;
    background: var(--accent);
  }
  .back-mark .brand-name {
    font-size: 40px;
    font-weight: 700;
    color: var(--text-light);
    letter-spacing: 0.5px;
  }
  .tagline-rule {
    position: absolute;
    left: 0; right: 0;
    top: 258px;
    display: flex;
    align-items: center;
  }
  .tagline-rule .rule {
    flex: 1;
    height: 2px;
    background: var(--accent);
  }
  .tagline {
    padding: 0 18px;
    font-size: 15px;
    color: var(--accent);
    letter-spacing: 0.3px;
    white-space: nowrap;
  }

  /* Front card */
  .holder-name {
    position: absolute;
    left: 50px;
    top: 150px;
    font-size: 24px;
    font-weight: 600;
    color: var(--accent);
  }
  .name-rule {
    position: absolute;
    left: 260px;
    right: 40px;
    top: 178px;
    height: 1px;
    background: var(--rule-dark);
  }
  .front-mark {
    position: absolute;
    right: 60px;
    top: 75px;
    display: flex;
    align-items: center;
    gap: 14px;
  }
  .front-mark .mark-dot { width: 26px; height: 26px; }
  .front-mark .brand-name {
    font-size: 30px;
    font-weight: 700;
    color: var(--text-light);
  }
  .contact-rule {
    position: absolute;
    left: 260px;
    right: 40px;
    top: 262px;
    height: 1px;
    background: var(--rule-dark);
  }
  .contact-list {
    position: absolute;
    right: 40px;
    top: 285px;
    list-style: none;
    text-align: right;
  }
  .contact-list li {
    display: flex;
    justify-content: flex-end;
    align-items: center;
    gap: 12px;
    font-size: 19px;
    line-height: 28px;
    color: var(--text-light);
  }
  .contact-list svg { width: 14px; height: 14px; flex: none; }
</style>
</head>
<body>
<main class="canvas">

  <section class="card card--back" aria-label="Card back">
    <div class="back-mark">
      <span class="mark-dot"></span>
      <span class="brand-name">Ridgeline Journeys</span>
    </div>
    <div class="tagline-rule">
      <span class="rule"></span>
      <span class="tagline">Adventure&nbsp; GPS Trails</span>
      <span class="rule"></span>
    </div>
  </section>

  <section class="card card--front" aria-label="Card front">
    <p class="holder-name">Kieran Folsby</p>
    <span class="name-rule"></span>
    <div class="front-mark">
      <span class="mark-dot"></span>
      <span class="brand-name">Ridgeline Journeys</span>
    </div>
    <span class="contact-rule"></span>
    <ul class="contact-list">
      <li>044-555 010 472
        <svg viewBox="0 0 14 14" aria-hidden="true"><path d="M1 4c0-2 2-3 6-3s6 1 6 3v1h-3V4H4v1H1z M3 6h8l2 6H1z" fill="var(--accent)"/></svg>
      </li>
      <li>kieran@ridgelinejourneys.com
        <svg viewBox="0 0 14 14" aria-hidden="true"><rect x="1" y="3" width="12" height="8" fill="var(--accent)"/><path d="M1 3l6 5 6-5" stroke="#111" stroke-width="1" fill="none"/></svg>
      </li>
      <li>www.ridgelinejourneys.comau
        <svg viewBox="0 0 14 14" aria-hidden="true"><g stroke="var(--accent)" stroke-width="2" fill="none"><path d="M6 8l-2 2a2 2 0 0 1-3-3l2-2"/><path d="M8 6l2-2a2 2 0 0 0-3-3L5 3"/><path d="M5 9l4-4"/></g></svg>
      </li>
    </ul>
  </section>

</main>
</body>
</html>
```